Law Firm Website (Designed in Wix)

A website designed using my Wix account.
A website for a generalist law firm based in Melbourne, Australia.
The areas of practice include:
Criminal Law
Family Law
Civil Litigation
Wills & Probate
PELIX Claims
The colour theme will be green, black and white.
Website will require the following elements:
1. Chat box
2. General Description of the practice
3. Practice Areas (for selection)
4. Calendar bookings for Microsoft Outlook
5. Email enquiries
6. Telephone enquiries
7. Business location map
8. Videos
9. Photos

The following website can be used as inspiration, however I am looking for a copy and paste version of this site:
brunhollowadvocates.com

Target Market(s)

People requiring a Lawyer for Criminal, Family, Wills and Probabte, Conveyancing and Civil Litigstion Matters

Industry/Entity Type

Legal Sector

Coding

Coded - Design and coding required

Number of Pages Required

5+ page

Font styles to use
Other font styles liked:
• Based on business card

Requirements
Must have
• Colours and theme based on business card

```html
<!DOCTYPE html>
<html lang="en">
<head>
<meta charset="utf-8">
<title>Thornvale Lawyers</title>
<link rel="stylesheet" href="https://fonts.googleapis.com/css2?family=Montserrat:wght@400;500;600;700&family=Oswald:wght@300;400;600;700&display=swap">
<style>
:root{
  --green:#1b7a2b;
  --green-dark:#0f4d19;
  --green-deep:#0b3a12;
  --green-light:#9fcfa2;
  --ink:#1b1b1b;
  --grey:#6b6b6b;
  --white:#ffffff;
  --line:#d9d9d9;
}
*{box-sizing:border-box;margin:0;padding:0}
html,body{width:1200px;height:4441px;overflow:hidden;background:var(--white)}
body{position:relative;font-family:"Montserrat",sans-serif;color:var(--ink)}
.abs{position:absolute}
.heading{font-family:"Oswald",sans-serif;font-size:34px;color:var(--ink);text-transform:uppercase;letter-spacing:.5px;text-align:center}
.heading b{font-weight:700}
.heading span{font-weight:300}
.heading-rule{position:absolute;width:64px;height:3px;background:var(--green)}

/* top bar */
.topbar-corner{left:0;top:0;width:310px;height:30px;background:var(--ink);clip-path:polygon(0 0,100% 0,92% 100%,0 100%)}
.social-dot{width:18px;height:18px;border-radius:50%;background:var(--white)}
.topbar-info{top:6px;font-size:12px;color:var(--ink);display:flex;align-items:center;gap:6px}
/* nav */
.brand{display:flex;align-items:center;gap:12px}
.brand-mark{width:44px;height:44px;border-radius:50%;border:3px solid var(--green)}
.brand-name{font-family:"Montserrat",sans-serif;font-weight:500;color:var(--green);line-height:1;letter-spacing:1px}
.nav{top:57px;left:466px;display:flex;gap:32px;font-size:12px;font-weight:500;text-transform:uppercase}
.nav a{color:var(--ink);text-decoration:none;position:relative}
.nav a.active:after{content:"";position:absolute;left:0;right:0;bottom:-8px;height:2px;background:var(--ink)}
.btn-contact{left:917px;top:46px;width:142px;height:40px;border-radius:20px;background:var(--green);color:var(--white);font-size:11px;font-weight:700;display:flex;align-items:center;justify-content:center}

/* hero */
.hero-photo{left:0;top:98px;width:1200px;height:610px;background:linear-gradient(120deg,#9aa3a8 0%,#c8c1b4 40%,#6d6a66 70%,#a9a49b 100%);clip-path:polygon(0 0,100% 0,100% 480px,50% 600px,0 480px)}
.hero-ring{left:69px;top:94px;width:518px;height:518px;border-radius:50%;background:rgba(255,255,255,.45)}
.hero-circle{left:87px;top:112px;width:482px;height:482px;border-radius:50%;background:var(--green);color:var(--white);text-align:center}
.hero-circle h1{position:absolute;top:133px;width:100%;font-size:36px;font-weight:600;line-height:50px}
.hero-circle p{position:absolute;top:238px;left:40px;right:40px;font-size:15px;line-height:25px}
.btn-chat{left:154px;top:310px;width:176px;height:40px;border-radius:20px;background:var(--white);color:var(--green);font-size:12px;font-weight:700;display:flex;align-items:center;justify-content:center}

/* about */
.about-ring{left:109px;top:797px;width:450px;height:450px;border-radius:50%;background:var(--green)}
.about-photo{left:132px;top:804px;width:430px;height:430px;border-radius:50%;background:linear-gradient(160deg,#b7bcc0,#6f7780 60%,#3b4049)}
.about-text{left:617px;top:870px;width:440px;font-size:13px;line-height:21px;color:var(--ink)}
.about-text h2{font-family:"Oswald",sans-serif;font-size:32px;color:var(--green);text-transform:uppercase;margin-bottom:12px;padding-left:6px}
.about-text h2 b{font-weight:700}.about-text h2 span{font-weight:300;color:var(--ink)}
.about-text h2{border-bottom:3px solid var(--green);display:inline-block;line-height:36px}
.tick-line{display:flex;gap:8px;margin-top:12px}
.btn-outline{left:620px;top:1134px;width:158px;height:38px;border:2px solid var(--green);border-radius:19px;color:var(--green);font-size:11px;font-weight:700;display:flex;align-items:center;justify-content:center}

/* practice */
.practice-band{left:0;top:1322px;width:1200px;height:348px;background:linear-gradient(180deg,var(--green) 0%,var(--green-dark) 35%,#0a1f0d 55%,#0a1f0d 55.5%,var(--green) 55.6%,var(--green) 100%)}
.practice-title{left:0;top:1368px;width:1200px;color:var(--white)}
.card{top:1483px;width:186px;height:258px;clip-path:polygon(0 0,100% 0,100% 212px,50% 100%,0 212px);color:var(--white);text-align:center}
.card.green{background:var(--green)}
.card.dark{background:#1f1f1f}
.card h3{margin-top:20px;font-family:"Oswald",sans-serif;font-size:19px;font-weight:600}
.card.dark h3{font-weight:400}
.card p{margin:8px 14px 0;font-size:10.5px;line-height:14px}
.card-icon{position:absolute;left:38px;top:117px;width:110px;height:110px;border-radius:50%;display:flex;align-items:center;justify-content:center}
.card.green .card-icon{background:#0e4417}
.card.dark .card-icon{background:#3d3d3d}

/* team */
.team-intro{left:300px;top:1868px;width:600px;text-align:center;font-size:14px;line-height:22px}
.member{border-radius:50%;background:linear-gradient(160deg,#cfcfcf,#7a7a7a)}
.member-name{font-size:13px;color:var(--grey);text-align:center;width:200px}
.member-ring{left:508px;top:1961px;width:164px;height:164px;border-radius:50%;border:4px solid var(--green);background:var(--white)}
.dot{width:12px;height:12px;border-radius:50%;background:var(--green)}

/* gallery */
.gallery-band{left:0;top:2295px;width:1200px;height:458px;background:#1c1c1c}
.gallery-item{top:2417px;width:242px;height:242px;border-radius:50%}
.pager{display:flex;gap:12px}
.pager i{width:11px;height:11px;border-radius:50%;background:#bdbdbd;display:block}

/* case studies */
.case-main{left:164px;top:2883px;width:422px;height:427px;background:#f7f7f7}
.case-main-img{width:422px;height:238px;background:linear-gradient(135deg,#d8d8d8,#8c8c8c 60%,#3e3e3e)}
.case-main-body{padding:20px 28px;font-size:12px;color:var(--grey);line-height:19px}
.meta{color:var(--green);font-size:12px;font-weight:500}
.case-main-body h4{color:var(--ink);font-size:17px;font-weight:600;line-height:24px;margin:8px 0}
.readmore{color:var(--green);font-weight:600;font-size:14px;margin-top:10px}
.case-side{left:610px;width:436px;height:207px;border:1px solid var(--line);background:var(--white)}
.case-side-img{position:absolute;left:0;top:0;width:196px;height:205px;background:linear-gradient(135deg,#8a6a4a,#c9b49a 50%,#4e3a2a);clip-path:polygon(0 0,85% 0,100% 100%,0 100%)}
.case-side-body{position:absolute;left:210px;top:22px;width:216px;font-size:11.5px;line-height:18px;color:var(--grey)}
.case-side-body .date{color:var(--green);font-weight:600;font-size:13px}
.case-side-body h5{color:var(--ink);font-size:15px;font-weight:700;line-height:19px;margin:8px 0}
.case-side-body .more{color:var(--green);font-weight:700;font-size:11px;margin-top:8px}

/* contact */
.contact-band{left:0;top:3417px;width:600px;height:720px;background:var(--green-light)}
.map{left:600px;top:3417px;width:600px;height:720px;background:linear-gradient(160deg,#e6ede4,#d8e7d6 50%,#eaeae2)}
.form-field{left:133px;width:446px;height:46px;border:1.5px solid var(--green-dark);font-size:14px;color:var(--ink);padding:12px 18px}
.btn-submit{left:243px;top:3829px;width:181px;height:47px;background:var(--green);color:var(--white);font-size:17px;font-weight:500;display:flex;align-items:center;justify-content:center}

/* footer */
.footer-col h6{font-size:15px;font-weight:600;text-transform:uppercase;color:var(--ink);margin-bottom:14px}
.footer-col{font-size:12px;line-height:26px;color:var(--ink)}
.divider{top:4100px;width:2px;height:200px;background:var(--green)}
.contact-item{display:flex;gap:14px;align-items:flex-start;font-size:11.5px;line-height:17px;margin-bottom:20px}
.icon-circle{width:30px;height:30px;border-radius:50%;background:var(--ink);flex:none;display:flex;align-items:center;justify-content:center}
.hours{display:grid;grid-template-columns:72px 1fr;font-size:12px;line-height:18.5px}
.copyright{left:0;top:4402px;width:1200px;text-align:center;font-size:11px;color:var(--ink)}
</style>
</head>
<body>

<!-- top bar -->
<div class="abs topbar-corner"></div>
<div class="abs social-dot" style="left:137px;top:5px"></div>
<div class="abs social-dot" style="left:166px;top:5px"></div>
<div class="abs social-dot" style="left:195px;top:5px"></div>
<div class="abs topbar-info" style="left:670px">
  <svg width="12" height="14" viewBox="0 0 12 14"><path d="M6 0a5 5 0 0 0-5 5c0 4 5 9 5 9s5-5 5-9a5 5 0 0 0-5-5zm0 7a2 2 0 1 1 0-4 2 2 0 0 1 0 4z" fill="#1b1b1b"/></svg>
  218 Larkspur Road, Melbourne VIC 3004
</div>
<div class="abs topbar-info" style="left:958px">
  <svg width="13" height="13" viewBox="0 0 24 24"><path d="M6.6 10.8a15 15 0 0 0 6.6 6.6l2.2-2.2a1 1 0 0 1 1-.25 11.4 11.4 0 0 0 3.6.57 1 1 0 0 1 1 1V20a1 1 0 0 1-1 1A17 17 0 0 1 3 4a1 1 0 0 1 1-1h3.5a1 1 0 0 1 1 1c0 1.25.2 2.45.57 3.6a1 1 0 0 1-.25 1z" fill="#1b1b1b"/></svg>
  1300 555 017
</div>

<!-- header -->
<div class="abs brand" style="left:138px;top:40px">
  <div class="brand-mark"></div>
  <div class="brand-name"><div style="font-size:25px">THORNVALE</div><div style="font-size:16px;letter-spacing:6px;margin-top:2px">LAWYERS</div></div>
</div>
<nav class="abs nav">
  <a class="active">Home</a><a>About Us</a><a>Lawyers</a><a>Pratice Areas</a><a>Cases</a>
</nav>
<div class="abs btn-contact">CONTACT US</div>

<!-- hero -->
<svg class="abs" style="left:0;top:560px" width="1200" height="160" viewBox="0 560 1200 160">
  <polygon points="0,572 600,698 1200,572 1200,590 600,716 0,590" fill="#1b7a2b"/>
</svg>
<div class="abs hero-photo" role="img" aria-label="Photo of lawyers meeting around a conference table"></div>
<div class="abs hero-ring"></div>
<div class="abs hero-circle">
  <h1>WELCOME TO<br>THORNVALE LAWYERS</h1>
  <p>Lorem Ipsum has been the industry's standard dummy text ever since the 1500s, when an un-</p>
  <div class="abs btn-chat">CHAT WITH US</div>
</div>

<!-- about -->
<div class="abs about-ring"></div>
<div class="abs about-photo" role="img" aria-label="Portrait photo of a smiling lawyer in a suit"></div>
<div class="abs about-text">
  <h2><b>About</b> <span>Us</span></h2>
  <p>Lorem ipsum dolor sit amet, consectetur adipiscing elit, sed do eius-mod tempor incididunt ut labore et dolore.</p>
  <p>magna aliqua. Ut enim ad minim veniam, quis nostrud exercitation ulla-mco laboris nisi ut aliquip ex ea commodo consequat. Duis aute irure dolor in reprehenderit in voluptate velit esse cillum dolore eu fugiat nulla pariatur. Excepteur sint occaecat cupidatat non proident, sunt in</p>
  <div class="tick-line">
    <svg width="16" height="16" viewBox="0 0 16 16" style="flex:none;margin-top:2px"><circle cx="8" cy="8" r="8" fill="#1b7a2b"/><path d="M4.5 8.2l2.3 2.3 4.7-4.8" stroke="#fff" stroke-width="1.8" fill="none"/></svg>
    <span>The industry's standard dummy text ever since the 1500s, when an unknown.</span>
  </div>
</div>
<div class="abs btn-outline">READ MORE</div>

<!-- practice areas -->
<div class="abs practice-band"></div>
<div class="abs heading practice-title" style="color:#fff"><b>Practice</b> <span>Areas</span></div>
<div class="heading-rule" style="left:532px;top:1416px;background:#fff"></div>

<div class="abs card green" style="left:105px">
  <h3>Criminal Law</h3>
  <p>Lorem ipsum dolor sit amet, consectetur adipiscing elit, sed do eiusmod tempor</p>
  <div class="card-icon"><svg width="56" height="56" viewBox="0 0 56 56" fill="none" stroke="#fff" stroke-width="2.5"><rect x="18" y="8" width="14" height="24" rx="2" transform="rotate(45 25 20)"/><path d="M30 25l16 16"/><rect x="8" y="44" width="24" height="6"/></svg></div>
</div>
<div class="abs card dark" style="left:307px">
  <h3>Family Law</h3>
  <p>Lorem ipsum dolor sit amet, consectetur adipiscing elit, sed do eiusmod tempor</p>
  <div class="card-icon"><svg width="56" height="56" viewBox="0 0 56 56" fill="none" stroke="#fff" stroke-width="2.5"><path d="M28 8v36M14 14h28M14 14l-7 14h14zM42 14l-7 14h14zM18 48h20"/></svg></div>
</div>
<div class="abs card green" style="left:509px">
  <h3>Civil Litigation</h3>
  <p>Lorem ipsum dolor sit amet, consectetur adipiscing elit, sed do eiusmod tempor</p>
  <div class="card-icon"><svg width="56" height="56" viewBox="0 0 56 56" fill="none" stroke="#fff" stroke-width="2.5"><path d="M28 6v38M12 14h32M12 14l-6 13h12zM44 14l-6 13h12zM16 44h24v6H16z"/></svg></div>
</div>
<div class="abs card dark" style="left:710px">
  <h3>Wills &amp; Probate</h3>
  <p>Lorem ipsum dolor sit amet, consectetur adipiscing elit, sed do eiusmod tempor</p>
  <div class="card-icon"><svg width="56" height="56" viewBox="0 0 56 56" fill="none" stroke="#fff" stroke-width="2.5"><path d="M14 6h22l8 8v34H14z"/><path d="M20 20h18M20 27h18M20 34h10"/><circle cx="40" cy="42" r="7"/><path d="M37 42l2 2 4-4"/></svg></div>
</div>
<div class="abs card green" style="left:910px">
  <h3>PELIX Claims</h3>
  <p>Lorem ipsum dolor sit amet, consectetur adipiscing elit, sed do eiusmod tempor</p>
  <div class="card-icon"><svg width="56" height="56" viewBox="0 0 56 56" fill="none" stroke="#fff" stroke-width="2.5"><path d="M12 8h24v40H12z"/><path d="M17 18h14M17 25h14M17 32h8"/><path d="M46 16L30 40l-4 4 1-6 16-24z"/></svg></div>
</div>

<!-- our team -->
<div class="abs heading" style="left:0;top:1808px;width:1200px"><b style="color:var(--green)">Our</b> <span>Team</span></div>
<div class="heading-rule" style="left:560px;top:1855px"></div>
<p class="abs team-intro">Lorem ipsum dolor sit amet, consectetur adipiscing elit, sed do eiusmod tempor incid-idunt ut labore et dolore.</p>

<svg class="abs" style="left:0;top:1990px" width="1200" height="130" viewBox="0 1990 1200 130" fill="none">
  <path d="M0 2068 Q120 2010 262 2005" stroke="#999" stroke-width="1.5" stroke-dasharray="4 4"/>
  <path d="M358 2008 Q440 2015 508 2036" stroke="#999" stroke-width="1.5" stroke-dasharray="4 4"/>
  <path d="M672 2085 Q760 2110 852 2110" stroke="#999" stroke-width="1.5" stroke-dasharray="4 4"/>
  <path d="M948 2110 Q1090 2100 1200 2050" stroke="#999" stroke-width="1.5" stroke-dasharray="4 4"/>
  <path d="M440 2034l-15 17 15 17M745 2034l15 17-15 17" stroke="#888" stroke-width="2"/>
</svg>
<div class="abs dot" style="left:60px;top:2039px"></div>
<div class="abs dot" style="left:694px;top:2090px"></div>
<div class="abs dot" style="left:1090px;top:2087px"></div>

<div class="abs member" style="left:262px;top:1957px;width:96px;height:96px" role="img" aria-label="Team member portrait"></div>
<div class="abs member-name" style="left:210px;top:2073px">MEMBER NAME</div>
<div class="abs member-ring"></div>
<div class="abs member" style="left:516px;top:1969px;width:148px;height:148px" role="img" aria-label="Featured team member portrait"></div>
<div class="abs" style="left:440px;top:2138px;width:300px;text-align:center;font-size:18px;font-weight:500;color:var(--green)">MEMBER NAME</div>
<div class="abs" style="left:440px;top:2170px;width:300px;text-align:center;font-size:11px;line-height:19px;color:var(--green)">ullamcorper est eget tempor cursus neque mi consectetuer mi a ultricies massa est sed nisl Class aptent taciti sociosqu ad litora</div>
<div class="abs member" style="left:852px;top:2064px;width:96px;height:96px" role="img" aria-label="Team member portrait"></div>
<div class="abs member-name" style="left:798px;top:2180px">MEMBER NAME</div>

<!-- gallery -->
<div class="abs gallery-band"></div>
<div class="abs heading" style="left:0;top:2332px;width:1200px;color:#fff"><b>Featured</b> <span>Gallery</span></div>
<div class="heading-rule" style="left:568px;top:2380px;background:#fff"></div>
<div class="abs gallery-item" style="left:96px;background:linear-gradient(135deg,#5f87a8,#2b3d52 60%,#8fb0c6)" role="img" aria-label="Photo of two lawyers reviewing documents in an office"></div>
<div class="abs gallery-item" style="left:355px;background:linear-gradient(135deg,#9a8e80,#e6e2dc 50%,#3a3a3a)" role="img" aria-label="Photo of lawyers in conversation"></div>
<div class="abs gallery-item" style="left:612px;background:linear-gradient(135deg,#d7dbe0,#4a5566 55%,#a8b0b8)" role="img" aria-label="Photo of colleagues working at a laptop"></div>
<div class="abs gallery-item" style="left:865px;background:linear-gradient(135deg,#6f6252,#b8a58c 50%,#2d3142)" role="img" aria-label="Photo of a lawyer at a desk with a gavel"></div>
<div class="abs pager" style="left:570px;top:2682px"><i></i><i style="background:#fff"></i><i style="background:#fff"></i></div>

<!-- case studies -->
<div class="abs heading" style="left:0;top:2792px;width:1200px"><span>Case</span> <b style="color:var(--green)">Studies</b></div>
<div class="heading-rule" style="left:560px;top:2840px"></div>

<div class="abs case-main">
  <div class="case-main-img" role="img" aria-label="Close-up photo of diamonds held by tweezers"></div>
  <div class="case-main-body">
    <div class="meta">April 12, 2019 &nbsp;|&nbsp; No Comments</div>
    <h4>Mauris vel lacus vitae felis vestibulum volutpat Etiam est</h4>
    <p>Nunc tempus felis vitae urna Vivamus porttitor neque at volutpat rutrum purus nisi eleifend libero a tempus libero lectus</p>
    <div class="readmore">Read More</div>
  </div>
</div>
<div class="abs case-side" style="top:2883px">
  <div class="case-side-img" role="img" aria-label="Photo of a boardroom with wooden furniture"></div>
  <div class="case-side-body">
    <div class="date">&#9641; 10 DEC 2018</div>
    <h5>Pellentesque faucibus Ut accumsa Donec</h5>
    <p>Duis quam Nam eget lacus Aliquam erat volutpat Quisque dignissim congue leoMauris vel lacus</p>
    <div class="more">READ MORE</div>
  </div>
</div>
<div class="abs case-side" style="top:3103px">
  <div class="case-side-img" style="background:linear-gradient(135deg,#4d4a48,#b6a894 50%,#6b5a48)" role="img" aria-label="Photo of a team meeting in a modern office"></div>
  <div class="case-side-body">
    <div class="date">&#9641; 10 DEC 2018</div>
    <h5>Pellentesque faucibus Ut accumsa Donec</h5>
    <p>Duis quam Nam eget lacus Aliquam erat volutpat Quisque dignissim congue leoMauris vel lacus</p>
    <div class="more">READ MORE</div>
  </div>
</div>
<div class="abs pager" style="left:570px;top:3345px"><i style="background:var(--ink)"></i><i style="background:var(--green)"></i><i style="background:var(--ink)"></i></div>

<!-- contact form + map -->
<div class="abs contact-band"></div>
<div class="abs map" role="img" aria-label="Street map of the office location on Larkspur Road, Melbourne"></div>
<svg class="abs" style="left:895px;top:3740px" width="22" height="30" viewBox="0 0 22 30"><path d="M11 0a11 11 0 0 0-11 11c0 8 11 19 11 19s11-11 11-19A11 11 0 0 0 11 0z" fill="#d93025"/><circle cx="11" cy="11" r="4" fill="#a11"/></svg>
<div class="abs heading" style="left:0;top:3475px;width:667px"><span>Case</span> <b style="color:var(--ink)">Studies</b></div>
<div class="heading-rule" style="left:302px;top:3524px;background:var(--green-dark)"></div>
<div class="abs form-field" style="top:3548px">Name</div>
<div class="abs form-field" style="top:3602px">Email address</div>
<div class="abs form-field" style="top:3656px">Subject</div>
<div class="abs form-field" style="top:3714px;height:96px">Message</div>
<div class="abs btn-submit">SUBMIT</div>

<!-- footer -->
<svg class="abs" style="left:0;top:3930px" width="1200" height="220" viewBox="0 3930 1200 220">
  <polygon points="0,4112 600,3939 1200,4112 1200,4150 0,4150" fill="#1b1b1b"/>
  <polygon points="0,4128 600,3958 1200,4128 1200,4150 0,4150" fill="#fff"/>
</svg>
<div class="abs brand" style="left:126px;top:4112px">
  <div class="brand-mark"></div>
  <div class="brand-name"><div style="font-size:25px;color:var(--ink)">THORNVALE</div><div style="font-size:16px;letter-spacing:6px;margin-top:2px">LAWYERS</div></div>
</div>
<div class="abs social-dot" style="left:127px;top:4192px;width:26px;height:26px;background:var(--ink)"></div>
<div class="abs social-dot" style="left:168px;top:4192px;width:26px;height:26px;background:var(--ink)"></div>
<div class="abs social-dot" style="left:209px;top:4192px;width:26px;height:26px;background:var(--ink)"></div>

<div class="abs divider" style="left:382px"></div>
<div class="abs divider" style="left:563px"></div>
<div class="abs divider" style="left:870px"></div>

<div class="abs footer-col" style="left:409px;top:4125px">
  <h6>Navigation</h6>
  <div>Home</div><div>About Us</div><div>Lawyers</div><div>Practice Areas</div><div>Contact Us</div>
</div>
<div class="abs footer-col" style="left:584px;top:4125px;width:280px">
  <h6>Contact Us</h6>
  <div class="contact-item"><div class="icon-circle"><svg width="14" height="14" viewBox="0 0 24 24"><path d="M6.6 10.8a15 15 0 0 0 6.6 6.6l2.2-2.2a1 1 0 0 1 1-.25 11.4 11.4 0 0 0 3.6.57 1 1 0 0 1 1 1V20a1 1 0 0 1-1 1A17 17 0 0 1 3 4a1 1 0 0 1 1-1h3.5a1 1 0 0 1 1 1c0 1.25.2 2.45.57 3.6a1 1 0 0 1-.25 1z" fill="#fff"/></svg></div><div>Phone<br>0400 555 219</div></div>
  <div class="contact-item"><div class="icon-circle"><svg width="14" height="12" viewBox="0 0 14 12"><rect x="1" y="1" width="12" height="10" fill="none" stroke="#fff" stroke-width="1.5"/><path d="M1 1l6 5 6-5" fill="none" stroke="#fff" stroke-width="1.5"/></svg></div><div>Email<br><span style="font-size:10.5px">enquiries@thornvalelawyers.com.au</span></div></div>
  <div class="contact-item"><div class="icon-circle"><svg width="11" height="14" viewBox="0 0 12 14"><path d="M6 0a5 5 0 0 0-5 5c0 4 5 9 5 9s5-5 5-9a5 5 0 0 0-5-5zm0 7a2 2 0 1 1 0-4 2 2 0 0 1 0 4z" fill="#fff"/></svg></div><div>Address<br>218 Larkspur Road, Melbourne VIC 3004</div></div>
</div>
<div class="abs footer-col" style="left:892px;top:4125px;width:250px">
  <h6>Working Hours</h6>
  <div class="hours">
    <span>Monday</span><span>9:00am - 5:00pm</span>
    <span>Tuesday</span><span>9:00am - 5:00pm</span>
    <span>Wednesday</span><span>9:00am - 5:00pm</span>
    <span>Thursday</span><span>9:00am - 5:00pm</span>
    <span>Friday</span><span>9:00am - 5:00pm</span>
    <span>Saturday</span><span>10:00am - 3:00pm</span>
    <span>Sunday</span><span>Closed</span>
  </div>
</div>
<div class="abs" style="left:0;top:4379px;width:1200px;height:1px;background:var(--line)"></div>
<div class="abs copyright">© 2023 Thornvale Lawyers. All Rights Reserved</div>

</body>
</html>
```